New Company Newsletter Template Needed!!!

We need some new graphics/design for us to create our company newsletter in MS Publisher/Word. Prefer simple, modern design that can be easy to update each month, flexible for adding images and include our company logo (attached).
Also attached our basic existing template but we do not want to use the same “swoosh” ribbon and want to reduce the number of colours used.
Needs to be elements we can move into the software and create a PDF newsletter to circulate.

Font styles to use
Sans Serif

Requirements
Must have
• Company logo
Nice to have
• If any colours should fit into our company logo palette

```html
<!DOCTYPE html>
<html lang="en">
<head>
<meta charset="utf-8">
<title>Brightway Newsletter — Issue #01</title>
<link href="https://fonts.googleapis.com/css2?family=Source+Sans+3:wght@400;600;700&display=swap" rel="stylesheet">
<style>
  :root {
    --navy: #233a80;
    --orange-light: #f39433;
    --orange-dark: #e8532e;
    --dot-red: #e8402f;
    --placeholder: #e6e7e8;
    --ink: #1a1a1a;
    --paper: #ffffff;
  }
  * { margin: 0; padding: 0; box-sizing: border-box; }
  html, body { width: 849px; height: 1200px; overflow: hidden; background: var(--paper); }
  body { font-family: "Source Sans 3", sans-serif; color: var(--ink); }

  .page { position: relative; width: 849px; height: 1200px; overflow: hidden; background: var(--paper); }
  .swooshes { position: absolute; inset: 0; width: 849px; height: 1200px; }

  .issue-number {
    position: absolute; right: 42px; top: 44px;
    color: var(--paper); font-weight: 700; font-size: 34px; letter-spacing: 0.5px;
  }

  .brand {
    position: absolute; left: 48px; top: 114px;
    display: flex; align-items: center; gap: 12px;
  }
  .brand-mark { width: 50px; height: 50px; border-radius: 50%; background: var(--orange-dark); }
  .brand-name { font-size: 48px; font-weight: 400; color: var(--navy); letter-spacing: -1px; line-height: 1; }

  .masthead {
    position: absolute; left: 36px; top: 197px;
    font-size: 89px; line-height: 1; color: var(--navy); letter-spacing: 2px;
    font-weight: 400;
  }
  .masthead strong { font-weight: 700; }

  .section-heading {
    position: absolute; left: 39px;
    display: flex; align-items: center; width: 770px;
    font-size: 33px; font-weight: 700; color: var(--navy); line-height: 1;
  }
  .section-heading .rule {
    flex: 1; height: 4px; margin-left: 22px; margin-top: 6px;
    background-image: radial-gradient(circle, var(--dot-red) 1.6px, transparent 1.9px);
    background-size: 14.5px 4px; background-repeat: repeat-x;
  }
  .heading-ceo { top: 313px; }
  .heading-activities { top: 661px; }

  .copy { position: absolute; font-size: 13.8px; line-height: 17.1px; }
  .ceo-col-1 { left: 38px; top: 370px; width: 240px; }
  .ceo-col-2 { left: 300px; top: 370px; width: 240px; }

  .photo { position: absolute; background: var(--placeholder); }
  .ceo-photo { left: 580px; top: 373px; width: 228px; height: 251px; }
  .activity-photo-1 { left: 39px; top: 714px; width: 227px; height: 212px; }
  .activity-photo-2 { left: 309px; top: 714px; width: 228px; height: 212px; }
  .activity-photo-3 { left: 580px; top: 714px; width: 228px; height: 141px; }
  .activity-photo-4 { left: 580px; top: 872px; width: 228px; height: 170px; }

  .caption-1 { left: 39px; top: 940px; width: 228px; text-align: center; }
  .caption-2 { left: 313px; top: 940px; width: 232px; }
  .caption-3 { left: 580px; top: 1053px; width: 235px; }
</style>
</head>
<body>
<div class="page">
  <svg class="swooshes" viewBox="0 0 849 1200" aria-hidden="true">
    <defs>
      <linearGradient id="band-top" x1="0" y1="0" x2="1" y2="0">
        <stop offset="0" stop-color="#f39433"/>
        <stop offset="1" stop-color="#e8532e"/>
      </linearGradient>
      <linearGradient id="band-bottom" x1="0" y1="0" x2="1" y2="0">
        <stop offset="0" stop-color="#e8532e"/>
        <stop offset="1" stop-color="#ef7a2d"/>
      </linearGradient>
    </defs>
    <path d="M0,0 L171,0 Q 85,45 0,110 Z" fill="var(--orange-light)"/>
    <path d="M171,0 Q 420,195 849,229 L849,0 Z" fill="var(--orange-light)"/>
    <path d="M186,0 Q 470,165 849,182 L849,0 Z" fill="url(#band-top)"/>
    <path d="M0,1064 Q 310,1075 479,1200 L0,1200 Z" fill="var(--orange-light)"/>
    <path d="M0,1108 Q 290,1115 442,1200 L0,1200 Z" fill="url(#band-bottom)"/>
  </svg>

  <div class="issue-number">ISSUE #01</div>

  <div class="brand">
    <span class="brand-mark"></span>
    <span class="brand-name">Brightway</span>
  </div>

  <h1 class="masthead"><strong>NEWS</strong>LETTER</h1>

  <h2 class="section-heading heading-ceo">Message from CEO<span class="rule"></span></h2>

  <p class="copy ceo-col-1">Lorem ipsum dolor sit amet, consectetuer adipiscing elit, sed diam nonummy nibh euismod tincidunt ut laoreet dolore magna aliquam erat volutpat. Ut wisi enim ad minim veniam, quis nostrud exerci tation ullamcorper suscipit lobortis nisl ut aliquip ex ea commodo consequat. Duis autem vel eum iriure dolor in hendrerit in vulputate velit esse molestie consequat, vel illum dolore eu feugiat nulla facilisis at vero eros et accumsan et iusto odio dignissim qui blandit praesent luptatum zzril delenit augue duis dolore te feugait nulla facilisi.</p>

  <p class="copy ceo-col-2">Lorem ipsum dolor sit amet, consectetuer adipiscing elit, sed diam nonummy nibh euismod tincidunt ut laoreet dolore magna aliquam erat volutpat. Ut wisi enim ad minim veniam, quis nostrud exerci tation ullamcorper suscipit lobortis nisl ut aliquip ex ea commodo consequat. Duis autem vel eum iriure dolor in hendrerit in vulputate velit esse molestie consequat, vel illum dolore eu feugiat nulla facilisis at vero eros et accumsan et iusto odio dignissim qui blandit praesent luptatum zzril delenit augue duis dolore te feugait nulla facilisi.</p>

  <div class="photo ceo-photo" role="img" aria-label="Photo of the CEO"></div>

  <h2 class="section-heading heading-activities">Activities<span class="rule"></span></h2>

  <div class="photo activity-photo-1" role="img" aria-label="Activity photo"></div>
  <div class="photo activity-photo-2" role="img" aria-label="Activity photo"></div>
  <div class="photo activity-photo-3" role="img" aria-label="Activity photo"></div>
  <div class="photo activity-photo-4" role="img" aria-label="Activity photo"></div>

  <p class="copy caption-1">Lorem ipsum dolor sit amet, consectetuer adipiscing elit, sed diam nonummy nibh euismod tincidunt ut laoreet dolore .</p>

  <p class="copy caption-2">Lorem ipsum dolor sit amet, consectetuer adipiscing elit, sed diam nonummy nibh euismod tincidunt ut laoreet dolore magna aliquam erat volutpat. Ut wisi enim ad minim veniam, quis nostrud exerci tation ullamcorper suscipit lobortis nisl ut aliquip ex ea commodo consequat.</p>

  <p class="copy caption-3">Lorem ipsum dolor sit amet, consectetuer adipiscing elit, sed diam nonummy nibh euismod tincidunt ut laoreet dolore magna aliquam erat volutpat. Ut wisi enim ad minim veniam.</p>
</div>
</body>
</html>
```